Veterinary company needs powerpoint design

Our veterinary company working with in vitro fertilization needs a professional power point design and business card design.
for the power point desing we would like frontpage, plain slides, table slides, figure slides etc.
the colours should be matching our logo in blue-ish: blue, purple, grey, turquoise
We like it minimalistic, elegant, serious but with a warm touch.

Target Market(s)

Academic,

Industry/Entity Type

Veterinary

Contact Information for Business Card

name, title, email, phone, website

Font styles to use
Sans Serif

Colors
0455a3
3277b5
85abd2
cfdeed
6b449b
886aae
b8a6cd
e4daeb
86cfc6

```html
<!DOCTYPE html>
<html lang="en">
<head>
<meta charset="utf-8">
<title>Nordvang Equine Fertility Labs – Presentation Template</title>
<link rel="stylesheet" href="https://fonts.googleapis.com/css2?family=Lato:ital,wght@0,400;0,700;0,900;1,700&family=Quicksand:wght@500;600;700&display=swap">
<style>
:root{
  --blue:#0455a3;
  --blue-mid:#3277b5;
  --blue-soft:#85abd2;
  --blue-pale:#cfdeed;
  --purple:#6b449b;
  --purple-mid:#886aae;
  --purple-soft:#b8a6cd;
  --purple-pale:#e4daeb;
  --turquoise:#86cfc6;
  --grey:#8c8c8c;
  --grey-light:#eeeeee;
  --ink:#222;
  --board:#ffffff;
  --rule:#e4e4e4;
}
*{box-sizing:border-box;margin:0;padding:0}
html,body{width:1200px;height:854px;overflow:hidden;background:var(--board)}
body{position:relative;font-family:"Lato",sans-serif;color:var(--ink)}
.row-rule{position:absolute;left:33px;width:1137px;height:1px;background:var(--rule)}
.slide{position:absolute;width:359px;height:202px;background:#fff;overflow:hidden;
  box-shadow:4px 6px 9px rgba(0,0,0,.35)}
.heading{font-family:"Quicksand",sans-serif;font-weight:700}
.photo{position:absolute}
.body-text{font-size:5.4px;line-height:1.45}
.body-text b{color:var(--blue)}

/* title band shared */
.band{position:absolute;left:0;right:0;background:var(--blue)}
.band-dot{position:absolute;width:7px;height:7px;border-radius:50%;background:#fff;border:1.5px solid var(--blue)}
.slide-title{position:absolute;left:37px;font-size:12px;color:var(--blue)}
.slide-subtitle{position:absolute;left:37px;font-size:9px;font-style:italic;font-weight:700;color:#fff}

/* cover */
.cover .photo{inset:0;background:linear-gradient(100deg,#9a9a9a 0%,#c9c9c9 40%,#7a7a7a 70%,#b0b0b0 100%)}
.cover-circle{position:absolute;left:33px;top:14px;width:172px;height:172px;border-radius:50%;
  background:rgba(4,85,163,.93);color:#fff;text-align:center}
.brand-mark{width:14px;height:14px;border-radius:50%;background:#fff;margin:40px auto 6px}
.brand-name{font-size:20px;font-weight:700;letter-spacing:1px;line-height:1}
.brand-sub{font-size:10px;font-weight:700;margin-top:2px}
.cover-name{font-size:6px;margin-top:12px;opacity:.85}
.cover-date{font-size:7px;font-weight:700;margin-top:5px}
.corner{position:absolute;width:10px;height:10px;border-color:rgba(255,255,255,.8);border-style:solid}

/* agenda */
.agenda-list{position:absolute;left:0;right:0;top:72px;bottom:0;background:#f3f3f3;padding-top:4px}
.agenda-item{display:flex;align-items:center;height:18px;margin-left:38px;border-bottom:1px solid #fff;font-size:5px;font-weight:700}
.agenda-num{width:16px;height:17px;background:var(--blue);color:#fff;display:flex;align-items:center;justify-content:center;margin-right:6px}

/* quote */
.quote{background:var(--blue);color:#fff}
.quote-title{position:absolute;top:40px;left:0;right:0;text-align:center;font-size:16px;font-weight:600}
.quote-mark{position:absolute;font-family:"Lato",sans-serif;font-weight:900;font-size:22px}
.quote p{position:absolute;left:88px;width:186px;font-size:4.6px;line-height:1.35;text-align:center}

/* features */
.features .photo{left:0;top:0;width:172px;height:202px;background:linear-gradient(160deg,#bdbdbd,#6e6e6e 55%,#d4d4d4)}
.features-panel{position:absolute;left:172px;top:0;right:0;bottom:0;background:var(--blue)}
.feature{position:absolute;left:16px;right:12px;height:34px;display:flex;align-items:center;gap:10px;color:#fff}
.feature-icon{width:34px;height:34px;border:1px solid #fff;flex:none;display:flex;align-items:center;justify-content:center}
.feature p{font-size:4.6px;line-height:1.35;border-bottom:1px solid rgba(255,255,255,.7);padding-bottom:3px}

/* columns */
.col{position:absolute;top:80px;width:136px}
.bullets{list-style:none}
.bullets li{position:relative;padding-left:7px;margin-bottom:4px}
.bullets li::before{content:"";position:absolute;left:0;top:1.5px;width:3px;height:3px;border-radius:50%;border:.6px solid var(--blue)}

/* timeline */
.tl-line{position:absolute;left:28px;right:20px;top:165px;height:1.5px;background:#333}
.tl-point{position:absolute}
.tl-stem{position:absolute;width:1.2px}
.tl-dot{position:absolute;width:7px;height:7px;border-radius:50%}
.tl-year{position:absolute;font-size:10px;font-weight:900;top:179px}
.tl-text{position:absolute;width:46px;font-size:4.2px;line-height:1.35}

/* headline icons */
.icon-col{position:absolute;top:78px;width:50px;text-align:center}
.icon-box{width:22px;height:22px;margin:0 auto;display:flex;align-items:center;justify-content:center}
.icon-dots{width:2px;height:12px;margin:3px auto;background:repeating-linear-gradient(var(--blue) 0 1.5px,transparent 1.5px 3.5px)}
.icon-col h4{font-size:4.2px;font-weight:700;line-height:1.3}
.icon-col .dash{width:10px;height:1.2px;margin:6px auto 3px}
.icon-col p{font-size:3.8px;line-height:1.3;color:#444}

/* thanks */
.thanks-top{position:absolute;left:0;right:0;top:0;height:83px;background:var(--blue)}
.thanks-title{position:absolute;top:30px;left:0;right:0;text-align:center;color:#fff;font-size:15px}
.thanks .photo{left:0;right:0;top:83px;bottom:0;background:linear-gradient(180deg,#8f8f8f 0%,#d9d9d9 45%,#9d9d9d 75%,#2a2a2a 100%)}
</style>
</head>
<body>

<div class="row-rule" style="top:294px"></div>
<div class="row-rule" style="top:567px"></div>

<!-- Cover -->
<section class="slide cover" style="left:33px;top:59px">
  <div class="photo" role="img" aria-label="Black and white photo of a woman with her horse in a meadow"></div>
  <span class="corner" style="left:14px;top:14px;border-width:1px 0 0 1px"></span>
  <span class="corner" style="right:14px;top:14px;border-width:1px 1px 0 0"></span>
  <span class="corner" style="left:14px;bottom:14px;border-width:0 0 1px 1px"></span>
  <span class="corner" style="right:14px;bottom:14px;border-width:0 1px 1px 0"></span>
  <div class="cover-circle">
    <div class="brand-mark"></div>
    <div class="brand-name">NORDVANG</div>
    <div class="brand-sub">Equine Fertility Labs</div>
    <div class="cover-name">Dr. &lt;Name&gt;</div>
    <div class="cover-date">July 27, 2019</div>
  </div>
</section>

<!-- Agenda -->
<section class="slide" style="left:422px;top:59px">
  <div class="band" style="top:0;height:47px"></div>
  <h2 class="heading" style="position:absolute;left:39px;top:14px;font-size:12px;color:#fff">Agenda</h2>
  <div style="position:absolute;left:28px;right:0;top:38px;height:1.2px;background:#fff"></div>
  <span class="band-dot" style="left:25px;top:35px;background:var(--blue);border-color:#fff"></span>
  <div class="agenda-list">
    <div class="agenda-item"><span class="agenda-num">1</span>Topic 1</div>
    <div class="agenda-item"><span class="agenda-num">2</span>Topic 2</div>
    <div class="agenda-item"><span class="agenda-num">3</span>Topic 3</div>
    <div class="agenda-item"><span class="agenda-num">4</span>Topic 4</div>
    <div class="agenda-item"><span class="agenda-num">5</span>Topic 5</div>
    <div class="agenda-item"><span class="agenda-num">6</span>Topic 6</div>
  </div>
</section>

<!-- Quote -->
<section class="slide quote" style="left:811px;top:59px">
  <span class="corner" style="left:50px;top:13px;width:14px;height:14px;border-width:1px 0 0 1px"></span>
  <span class="corner" style="right:50px;top:13px;width:14px;height:14px;border-width:1px 1px 0 0"></span>
  <span class="corner" style="left:50px;bottom:13px;width:14px;height:14px;border-width:0 0 1px 1px"></span>
  <span class="corner" style="right:50px;bottom:13px;width:14px;height:14px;border-width:0 1px 1px 0"></span>
  <span class="quote-mark" style="left:66px;top:44px">&ldquo;</span>
  <span class="quote-mark" style="right:64px;top:132px">&rdquo;</span>
  <h2 class="heading quote-title" style="top:40px">Quote or Headline</h2>
  <p style="top:66px"><b>Lorem ipsum dolor</b> sit amet, consectetur adipiscing elit, sed do eiusmod tempor incididunt ut labore et dolore magna aliqua. Ut enim ad minim veniam, quis nostrud exercitation ullamco laboris nisi ut aliquip ex ea commodo consequat. Duis aute irure dolor in reprehenderit in voluptate velit esse cillum dolore eu fugiat nulla pariatur. Excepteur sint occaecat cupidatat non proident, sunt in culpa officia deserunt mollit anim id est.</p>
  <p style="top:114px"><b>Lorem ipsum dolor</b> sit amet, consectetur adipiscing elit, sed do eiusmod tempor incididunt ut labore et dolore magna aliqua. Ut enim ad minim veniam, quis nostrud exercitation ullamco laboris nisi ut aliquip ex ea commodo consequat. Duis aute irure dolor in reprehenderit in voluptate velit esse cillum dolore eu fugiat nulla pariatur. Excepteur sint occaecat cupidatat non proident, sunt in culpa officia deserunt mollit anim id est.</p>
</section>

<!-- Features -->
<section class="slide features" style="left:33px;top:326px">
  <div class="photo" role="img" aria-label="Black and white close-up of a rider's boot in a stirrup"></div>
  <div class="features-panel">
    <div class="feature" style="top:42px">
      <div class="feature-icon"><svg width="20" height="20" viewBox="0 0 20 20" fill="none" stroke="#fff" stroke-width="1.1"><circle cx="10" cy="7" r="3.5"/><path d="M3 18c0-4 3-6 7-6s7 2 7 6"/><path d="M8 12l2 3 2-3"/></svg></div>
      <p><b>Lorem ipsum dolor</b> sit amet, consectetur adipiscing elit, sed do eiusmod tempor incididunt ut labore et dolore magna aliqua. Ut enim ad minim veniam, quis nostrud exercitation ullamco laboris nisi ut aliquip ex ea commodo consequat.</p>
    </div>
    <div class="feature" style="top:84px">
      <div class="feature-icon"><svg width="20" height="20" viewBox="0 0 20 20" fill="none" stroke="#fff" stroke-width="1.1"><rect x="4" y="3" width="11" height="14"/><path d="M6 7h7M6 10h7M6 13h4"/><path d="M16 8l-5 7"/></svg></div>
      <p><b>Lorem ipsum dolor</b> sit amet, consectetur adipiscing elit, sed do eiusmod tempor incididunt ut labore et dolore magna aliqua. Ut enim ad minim veniam, quis nostrud exercitation ullamco laboris nisi ut aliquip ex ea commodo consequat.</p>
    </div>
    <div class="feature" style="top:126px">
      <div class="feature-icon"><svg width="20" height="20" viewBox="0 0 20 20" fill="none" stroke="#fff" stroke-width="1.1"><path d="M3 8h4l8-4v12l-8-4H3z"/><path d="M5 12l1.5 5H9l-1-5"/></svg></div>
      <p><b>Lorem ipsum dolor</b> sit amet, consectetur adipiscing elit, sed do eiusmod tempor incididunt ut labore et dolore magna aliqua. Ut enim ad minim veniam, quis nostrud exercitation ullamco laboris nisi ut aliquip ex ea commodo consequat.</p>
    </div>
  </div>
</section>

<!-- Title + text with bullets -->
<section class="slide" style="left:422px;top:326px">
  <h2 class="heading slide-title" style="top:17px">Title</h2>
  <div class="band" style="top:46px;height:20px"></div>
  <span class="band-dot" style="left:30px;top:43px"></span>
  <div class="slide-subtitle" style="top:50px">Subtitle</div>
  <div class="col body-text" style="left:37px">Lorem ipsum dolor sit amet, consectetur adipiscing elit, sed do. eiusmod tempor incididunt ut labore et dolore magna aliqua. Quis ipsum suspendisse ultrices gravida. Risus commodo viverra maecenas accumsan lacus vel facilisis. eiusmod tempor incididunt ut labore et dolore magna aliqua. Quis ipsum suspendisse ultrices gravida. Risus commodo viverra maecenas accumsan lacus vel facilisis. eiusmod tempor incididunt ut labore et dolore magna aliqua. Quis ipsum suspendisse ultrices gravida.</div>
  <ul class="col body-text bullets" style="left:205px;width:130px">
    <li><b>Lorem ipsum dolor</b> sit amet, consectetur adipiscing elit, sed do.</li>
    <li><b>Eiusmod tempor</b> incididunt ut labore</li>
    <li><b>Suspendisse ultrices</b> gravida. incididunt ut labore et dolore magna aliqua. Quis ipsum gra</li>
    <li><b>Viverra maecenas</b> accumsan lacus</li>
    <li><b>Incididunt ut labore</b> et dolore magna aliqua. Quis ipsum suspendisse.</li>
  </ul>
</section>

<!-- Timeline -->
<section class="slide" style="left:811px;top:326px">
  <h2 class="heading slide-title" style="top:17px">Timeline</h2>
  <div class="band" style="top:42px;height:20px"></div>
  <span class="band-dot" style="left:30px;top:39px"></span>
  <div class="tl-text" style="left:26px;top:123px"><b>Lorem ipsum dolor</b> sit amet, consectetur adipiscing elit, sed do eiusmod tempor incididunt ut labore et dolore magna aliqua.</div>
  <div class="tl-line"></div>

  <span class="tl-stem" style="left:78px;top:91px;height:75px;background:var(--blue)"></span>
  <span class="tl-dot" style="left:75px;top:88px;background:var(--blue);width:6px;height:6px"></span>
  <span class="tl-dot" style="left:75px;top:162px;background:var(--blue)"></span>
  <div class="tl-text" style="left:84px;top:90px"><b style="color:var(--blue)">Lorem ipsum dolor</b> sit amet, consectetur adipiscing elit, sed do eiusmod tempor incididunt ut labore et dolore magna aliqua. Ut enim ad minim veniam, quis nostrud exercitation ullamco laboris nisi ut aliquip ex ea commodo consequat.</div>
  <div class="tl-year" style="left:66px;color:var(--blue)">2017</div>

  <span class="tl-stem" style="left:144px;top:130px;height:36px;background:var(--grey)"></span>
  <span class="tl-dot" style="left:141px;top:127px;background:var(--grey);width:6px;height:6px"></span>
  <span class="tl-dot" style="left:141px;top:162px;background:var(--grey)"></span>
  <div class="tl-text" style="left:150px;top:125px;color:#777"><b>Lorem ipsum dolor</b> sit amet, consectetur adipiscing elit, sed do eiusmod tempor incididunt ut labore et dolore magna aliqua.</div>
  <div class="tl-year" style="left:132px;color:var(--grey)">2018</div>

  <span class="tl-stem" style="left:211px;top:91px;height:75px;background:var(--purple)"></span>
  <span class="tl-dot" style="left:208px;top:88px;background:var(--purple);width:6px;height:6px"></span>
  <span class="tl-dot" style="left:208px;top:162px;background:var(--purple)"></span>
  <div class="tl-text" style="left:217px;top:90px"><b style="color:var(--purple)">Lorem ipsum dolor</b> sit amet, consectetur adipiscing elit, sed do eiusmod tempor incididunt ut labore et dolore magna aliqua. Ut enim ad minim veniam, quis nostrud exercitation ullamco laboris nisi ut aliquip ex ea commodo consequat.</div>
  <div class="tl-year" style="left:199px;color:var(--purple)">2019</div>

  <span class="tl-stem" style="left:278px;top:130px;height:36px;background:var(--purple-mid)"></span>
  <span class="tl-dot" style="left:275px;top:127px;background:var(--purple-mid);width:6px;height:6px"></span>
  <span class="tl-dot" style="left:275px;top:162px;background:var(--purple-mid)"></span>
  <div class="tl-text" style="left:284px;top:125px"><b style="color:var(--purple-mid)">Lorem ipsum dolor</b> sit amet, consectetur adipiscing elit, sed do eiusmod tempor incididunt ut labore et dolore magna aliqua.</div>
  <div class="tl-year" style="left:266px;color:var(--purple-mid)">2020</div>
</section>

<!-- Headline with icons -->
<section class="slide" style="left:33px;top:592px">
  <h2 class="heading slide-title" style="top:17px">Headline</h2>
  <div class="band" style="top:42px;height:20px"></div>
  <span class="band-dot" style="left:30px;top:39px"></span>

  <div class="icon-col" style="left:47px">
    <div class="icon-box" style="background:var(--blue)"><svg width="12" height="12" viewBox="0 0 12 12" fill="none" stroke="#fff" stroke-width=".9"><circle cx="6" cy="4" r="2"/><path d="M2 11c0-2.5 2-4 4-4s4 1.5 4 4"/></svg></div>
    <div class="icon-dots"></div>
    <h4 style="color:var(--blue)">Lorem ipsum dolor sit amet, consectetur adipiscing elit, sed do eiusmod tempor</h4>
    <div class="dash" style="background:var(--blue)"></div>
    <p>Lorem ipsum dolor sit amet, consectetur adipiscing elit, sed do eiusmod tempor incididunt ut labore</p>
  </div>
  <div class="icon-col" style="left:103px">
    <div class="icon-box" style="background:var(--blue-soft)"><svg width="12" height="12" viewBox="0 0 12 12" fill="none" stroke="#fff" stroke-width=".9"><rect x="2" y="2" width="8" height="8"/><path d="M4 5h4M4 7h3"/></svg></div>
    <div class="icon-dots" style="background:repeating-linear-gradient(var(--blue-soft) 0 1.5px,transparent 1.5px 3.5px)"></div>
    <h4 style="color:var(--blue-soft)">Lorem ipsum dolor sit amet, consectetur adipiscing elit, sed do eiusmod tempor</h4>
    <div class="dash" style="background:var(--blue-soft)"></div>
    <p>Lorem ipsum dolor sit amet, consectetur adipiscing elit, sed do eiusmod tempor incididunt ut labore</p>
  </div>
  <div class="icon-col" style="left:158px">
    <div class="icon-box" style="background:var(--purple)"><svg width="12" height="12" viewBox="0 0 12 12" fill="none" stroke="#fff" stroke-width=".9"><path d="M2 5h2l5-2.5v7L4 7H2z"/></svg></div>
    <div class="icon-dots" style="background:repeating-linear-gradient(var(--purple) 0 1.5px,transparent 1.5px 3.5px)"></div>
    <h4 style="color:var(--purple)">Lorem ipsum dolor sit amet, consectetur adipiscing elit, sed do eiusmod tempor</h4>
    <div class="dash" style="background:var(--purple)"></div>
    <p>Lorem ipsum dolor sit amet, consectetur adipiscing elit, sed do eiusmod tempor incididunt ut labore</p>
  </div>
  <div class="icon-col" style="left:214px">
    <div class="icon-box" style="background:var(--purple-pale)"><svg width="12" height="12" viewBox="0 0 12 12" fill="none" stroke="#fff" stroke-width=".9"><circle cx="6" cy="6" r="4"/><path d="M6 3.5V6l2 1.5"/></svg></div>
    <div class="icon-dots" style="background:repeating-linear-gradient(var(--purple-pale) 0 1.5px,transparent 1.5px 3.5px)"></div>
    <h4 style="color:var(--purple-soft)">Lorem ipsum dolor sit amet, consectetur adipiscing elit, sed do eiusmod tempor</h4>
    <div class="dash" style="background:var(--purple-pale)"></div>
    <p style="color:#aaa">Lorem ipsum dolor sit amet, consectetur adipiscing elit, sed do eiusmod tempor incididunt ut labore</p>
  </div>
  <div class="icon-col" style="left:269px">
    <div class="icon-box" style="background:#cdeee9"><svg width="12" height="12" viewBox="0 0 12 12" fill="none" stroke="var(--turquoise)" stroke-width=".9"><circle cx="6" cy="6" r="4"/><circle cx="6" cy="6" r="1.8"/></svg></div>
    <div class="icon-dots" style="background:repeating-linear-gradient(var(--turquoise) 0 1.5px,transparent 1.5px 3.5px)"></div>
    <h4 style="color:var(--turquoise)">Lorem ipsum dolor sit amet, consectetur adipiscing elit, sed do eiusmod tempor</h4>
    <div class="dash" style="background:var(--turquoise)"></div>
    <p>Lorem ipsum dolor sit amet, consectetur adipiscing elit, sed do eiusmod tempor incididunt ut labore</p>
  </div>
</section>

<!-- Title + two columns -->
<section class="slide" style="left:422px;top:592px">
  <h2 class="heading slide-title" style="top:17px">Title</h2>
  <div class="band" style="top:46px;height:20px"></div>
  <span class="band-dot" style="left:30px;top:43px"></span>
  <div class="slide-subtitle" style="top:50px">Subtitle</div>
  <div class="col body-text" style="left:37px">Lorem ipsum dolor sit amet, consectetur adipiscing elit, sed do. eiusmod tempor incididunt ut labore et dolore magna aliqua. Quis ipsum suspendisse ultrices gravida. Risus commodo viverra maecenas accumsan lacus vel facilisis. eiusmod tempor incididunt ut labore et dolore magna aliqua. Quis ipsum suspendisse ultrices gravida. Risus commodo viverra maecenas accumsan lacus vel facilisis. eiusmod tempor incididunt ut labore et dolore magna aliqua. Quis ipsum suspendisse ultrices gravida.</div>
  <div class="col body-text" style="left:196px">Lorem ipsum dolor sit amet, consectetur adipiscing elit, sed do. eiusmod tempor incididunt ut labore et dolore magna aliqua. Quis ipsum suspendisse ultrices gravida. Risus commodo viverra maecenas accumsan lacus vel facilisis. eiusmod tempor incididunt ut labore et dolore magna aliqua. Quis ipsum suspendisse ultrices gravida. Risus commodo viverra maecenas accumsan lacus vel facilisis. eiusmod tempor incididunt ut labore et dolore magna aliqua. Quis ipsum suspendisse ultrices gravida.</div>
</section>

<!-- Thank you -->
<section class="slide thanks" style="left:811px;top:592px">
  <div class="thanks-top"></div>
  <h2 class="heading thanks-title">Thank you!</h2>
  <div class="photo" role="img" aria-label="Black and white landscape of horses grazing on a hill under a cloudy sky"></div>
</section>

</body>
</html>
```